Car wrap desgin Sandmor

We’d like new design proposals for passenger cars (KD Orvel & Dalmo Ruvek eX). Both vehicles are white. I don’t want the entire car to be wrapped in yellow. more informations about us, you will find under: https://www.sandmooor.ch/home

Less is more. Keep it simple, clean, and stylish - and only with yellow ond black as color beside the with car

```html
<!DOCTYPE html>
<html lang="de">
<head>
<meta charset="utf-8">
<title>Sandmor – Fahrzeugbeschriftung</title>
<link rel="stylesheet" href="https://fonts.googleapis.com/css2?family=Barlow:wght@500;700&display=swap">
<style>
  :root {
    --page: #e6e7e9;
    --body-white: #ffffff;
    --panel-edge: #d2d4d7;
    --brand-yellow: #f2d21c;
    --brand-black: #141414;
    --tagline-grey: #4a4a4a;
  }
  * { box-sizing: border-box; margin: 0; padding: 0; }
  html, body {
    width: 1200px; height: 824px; overflow: hidden;
    background: var(--page);
    font-family: "Barlow", Arial, sans-serif;
  }
  .sheet {
    position: relative; width: 1200px; height: 824px;
    padding: 40px 28px; display: flex; flex-direction: column; gap: 16px;
  }
  .view {
    position: relative; flex: 1;
    display: flex; gap: 16px;
  }
  .surface {
    position: relative; flex: 1;
    background: var(--body-white);
    border: 1px solid var(--panel-edge);
    border-radius: 18px; overflow: hidden;
  }
  .surface--rear { flex: 0 0 380px; }
  .band {
    position: absolute; left: 0; right: 0; bottom: 0; height: 32%;
    background: var(--brand-yellow);
    clip-path: polygon(6% 0, 100% 0, 100% 100%, 0 100%, 0 38%);
  }
  .strip {
    position: absolute; left: 0; right: 0; bottom: 40px; height: 8px;
    background: var(--brand-yellow);
  }
  .lettering {
    position: absolute; left: 50%; top: 22%;
    transform: translateX(-50%);
    text-align: left;
  }
  .brand-name {
    font-weight: 700; color: var(--brand-black);
    font-size: 58px; letter-spacing: 1px; line-height: 1;
  }
  .tagline {
    margin-top: 12px;
    font-weight: 500; color: var(--tagline-grey);
    font-size: 17px; letter-spacing: 2.2px;
  }
  .rear-lettering {
    position: absolute; left: 50%; top: 28%;
    transform: translateX(-50%); text-align: center;
  }
  .rear-lettering .brand-name { font-size: 38px; }
  .web {
    margin-top: 16px;
    font-weight: 500; color: var(--tagline-grey);
    font-size: 15px; letter-spacing: 0.5px;
  }
</style>
</head>
<body>
  <main class="sheet">
    <section class="view view--side" aria-label="Seitenansicht">
      <div class="surface surface--side">
        <div class="lettering">
          <p class="brand-name">SANDMOOOR</p>
          <p class="tagline">HAUSTECHNIK + BAUSPENGLEREI</p>
        </div>
        <div class="band"></div>
      </div>
    </section>

    <section class="view view--rear" aria-label="Heck- und Seitenansicht">
      <div class="surface surface--rear">
        <div class="rear-lettering">
          <p class="brand-name">SANDMOOOR</p>
          <p class="web">www.sandmooor.ch</p>
        </div>
        <div class="strip"></div>
      </div>
      <div class="surface surface--side">
        <div class="lettering">
          <p class="brand-name">SANDMOOOR</p>
          <p class="tagline">HAUSTECHNIK + BAUSPENGLEREI</p>
        </div>
        <div class="band"></div>
      </div>
    </section>
  </main>
</body>
</html>
```